詳細はzipファイルにまとめておりおますので、こちらからダウンロードしてください。

http://3.hakobuya.nu/0522-k83920fa17de462093b8e1c7f06a35d9

【デザインの参考サイト】
クライアント様からは、以下の参考サイトを挙げていただいております。
http://plumtivra.com/
https://sorvik4417.com/

ただし、上記サイトはおしゃれではあるものの、少しアピールが弱いようにも思います。
最終的な成果(査定依頼や、来店予約)に結びつきやすいような工夫があれば嬉しいです。

【継続発注について】
まずはトップページのみのデザインをお願い致します。
トップページのデザインが決まりましたら、下層ページのデザインもお願いする予定です。(1ページ1~2万円程度の予定)
下層ページは2~3ページほどの予定ですので、総額12万円ぐらいの予定です。

【スマホ対応について】
コーディング時に、レスポンシブ対応する予定ですので、スマホ対応しやすいデザインにしていただければ助かります。

【レイアウトの変更などについて】
基本的にはワイヤーに沿って作っていただければと思います。
ただし、「もっとこうしたほうが良いのでは?」「こんな形はどうか?」といったようなご提案があれば、別途ご相談ください。

必要な資料は上記のzipファイルの中に入れておりますので、そちらをご覧ください。
もし不明な点があれば遠慮なくご連絡くださいませ。
1ページ
シンプル 複雑
単色 カラフル
暗い 明るい
日常 高級
遊び心 厳粛
未来的 伝統的
女性的 男性的
黄・オレンジ系
• 高解像度JPG (.jpg)
• イラストレーター形式 (.ai)
納品は、IllustratorでもPhotoshopでもFireworksでも、どのファイルでもOKです。

また、納品の際には使っているフォントをお教えください。
(使用フォントはモリサワ、もしくはフリーフォントでお願いします)
たくさんのご応募ありがとうございました。
非常に悩んだのですが、お一人の方を選ばせていただきました。
選に漏れた方々につきましては、お手数おかけしたにも関わらず何もお返しできずに心苦しくもあるのですが、ご了承いただければ幸いです。
またこれに懲りず、今後ともよろしくお願いいたします。
ありがとうございました!

いいデザインをしていただいた方が数人おられて、非常に悩みました。
その中で一番こちらの意図を汲み取っていただき、バランスの取れたデザインをしていただいた、ということで、こちらの方にお願いすることにしました。

たくさんのご応募ありがとうございました。
ありがとうございました!

```html
<!DOCTYPE html>
<html lang="ja">
<head>
<meta charset="utf-8">
<title>タカミエ | 7階以上の新築、買い取ります。</title>
<link rel="stylesheet" href="https://fonts.googleapis.com/css2?family=Noto+Sans+JP:wght@400;500;700;900&family=Montserrat:wght@600;700;800&display=swap">
<style>
:root{
  --yellow:#f5d800;
  --yellow-soft:#fff3a6;
  --ink:#222222;
  --text:#444444;
  --muted:#888888;
  --line:#dddddd;
  --grey:#eeeeee;
  --green:#8cc63f;
  --green-dark:#5f9a1f;
  --footer:#2b2b2b;
  --white:#ffffff;
}
*{box-sizing:border-box;margin:0;padding:0}
html,body{width:1200px;height:4588px;overflow:hidden}
body{font-family:"Noto Sans JP",sans-serif;color:var(--text);background:var(--white);position:relative;font-size:13px;line-height:1.7}
.section{position:absolute;left:0;width:1200px}
.brand{font-family:"Noto Sans JP",sans-serif;font-weight:900;color:var(--ink);letter-spacing:2px}

/* header */
.site-header{top:0;height:64px;background:var(--white);display:flex;align-items:center;padding:0 0 0 30px;border-bottom:1px solid var(--line)}
.site-header .brand{font-size:28px;display:flex;align-items:center;gap:8px}
.site-header .brand i{display:block;width:10px;height:10px;background:var(--yellow)}
.site-header .tagline{font-size:10px;line-height:1.4;color:var(--text);margin-left:14px;border-left:1px solid var(--line);padding-left:12px}
.global-nav{margin-left:auto;display:flex;align-items:center;height:100%}
.global-nav a{font-size:12px;color:var(--ink);text-decoration:none;padding:0 22px;font-weight:500}
.btn-reserve{height:64px;width:150px;background:var(--yellow);display:flex;align-items:center;justify-content:center;gap:8px;font-weight:700;color:var(--ink);font-size:14px}

/* hero */
.hero{top:64px;height:500px;background:linear-gradient(100deg,#c8d2d9 0%,#e9eef1 35%,#f4f2ee 60%,#d8d1c6 100%)}
.hero-copy{position:absolute;top:40px;left:0;width:100%;text-align:center}
.hero-copy p{font-size:24px;font-weight:700;color:var(--ink);letter-spacing:2px}
.hero-copy .brand{font-size:52px;margin-top:6px;display:inline-flex;align-items:center;gap:12px}
.hero-copy .brand i{width:16px;height:16px;background:var(--yellow);display:block}
.slider-dots{top:572px;height:16px;display:flex;justify-content:center;gap:10px}
.slider-dots span{width:9px;height:9px;border-radius:50%;background:#ccc}
.slider-dots span:first-child{background:#555}

/* intro */
.intro{top:600px;height:290px;background:linear-gradient(180deg,#ffffff 0%,#eef4f9 50%,#dde9f2 100%);display:flex;align-items:center;justify-content:center;text-align:center}
.intro p{font-size:14px;line-height:2.2;color:var(--ink);width:760px}

/* points */
.points{top:920px;height:500px;background:linear-gradient(180deg,#b9b6b1 0%,#d6d3ce 45%,#e7e5e1 100%)}
.point-list{position:absolute;top:40px;left:170px;width:860px;display:flex;gap:25px}
.point-card{width:270px;background:var(--white);border:3px solid var(--yellow)}
.point-card .point-head{background:var(--yellow);padding:14px 14px 12px;display:flex;gap:10px;align-items:center}
.point-tag{background:var(--ink);color:var(--white);font-family:"Montserrat",sans-serif;font-weight:700;text-align:center;width:54px;padding:4px 0;line-height:1.1}
.point-tag small{display:block;font-size:9px;letter-spacing:1px}
.point-tag b{font-size:22px}
.point-head h3{font-size:14px;color:var(--ink);line-height:1.5}
.point-card p{padding:14px 16px 18px;font-size:12px;line-height:1.9}
.about-box{position:absolute;top:330px;left:450px;width:300px;background:var(--white);border:2px solid var(--ink);padding:18px 0 20px;text-align:center}
.about-box h2{font-size:18px;color:var(--ink);font-weight:700}
.about-box h2 .brand{font-size:22px;margin-right:4px}
.btn-yellow{display:inline-flex;align-items:center;justify-content:center;gap:10px;background:var(--yellow);color:var(--ink);font-weight:700;font-size:14px;border:2px solid var(--ink)}
.about-box .btn-yellow{margin-top:12px;width:230px;height:44px}

/* heading */
.slant-heading{position:absolute;left:0;width:100%;display:flex;justify-content:center;align-items:center;gap:18px;font-size:20px;font-weight:700;color:var(--ink)}
.en-heading{position:absolute;left:0;width:100%;text-align:center}
.en-heading h2{font-family:"Montserrat",sans-serif;font-weight:800;font-size:30px;letter-spacing:6px;color:var(--ink);display:inline-block;border-bottom:4px solid var(--ink);padding:0 12px 2px}
.en-heading p{font-size:11px;color:var(--muted);margin-top:6px}

/* compare */
.compare{top:1440px;height:700px}
.compare .slant-heading{top:20px}
.compare-col{position:absolute;top:110px}
.col-sites{left:170px;width:420px;height:540px;background:var(--grey);padding:26px 26px}
.col-ours{left:620px;width:410px;height:540px;padding:0 26px}
.col-title{display:inline-block;border:2px solid var(--ink);background:var(--white);padding:4px 26px;font-weight:700;color:var(--ink);font-size:15px}
.col-ours .col-title{border-color:var(--yellow);background:var(--yellow-soft)}
.diagram{display:block;margin:16px auto 0}
.reasons{list-style:none;margin-top:14px}
.reasons li{font-size:12px;line-height:1.8;padding-left:26px;position:relative;margin-bottom:10px}
.reasons li b{position:absolute;left:0;top:2px;width:18px;height:18px;border-radius:50%;background:var(--ink);color:var(--white);font-size:10px;text-align:center;line-height:18px}

/* faq */
.faq{top:2170px;height:700px;background:#f6f6f6}
.faq .en-heading{top:60px}
.faq-list{position:absolute;top:160px;left:170px;width:860px;display:grid;grid-template-columns:repeat(3,270px);gap:30px 25px}
.faq-card{background:var(--white);border:2px solid var(--ink)}
.faq-q{background:var(--yellow);display:flex;gap:10px;padding:12px 12px;border-bottom:2px solid var(--ink)}
.faq-a{display:flex;gap:10px;padding:12px 12px 16px}
.faq-card .mark{flex:none;width:26px;height:26px;background:var(--ink);color:var(--white);font-family:"Montserrat",sans-serif;font-weight:700;font-size:15px;display:flex;align-items:center;justify-content:center}
.faq-a .mark{background:var(--white);color:var(--ink);border:2px solid var(--ink)}
.faq-q p{font-size:12px;font-weight:700;color:var(--ink);line-height:1.6}
.faq-a p{font-size:11.5px;line-height:1.8}

/* results */
.results{top:2900px;height:1040px}
.results .en-heading{top:50px}
.result-list{position:absolute;top:150px;left:170px;width:860px}
.result-item{display:flex;gap:26px;height:240px;padding:20px 0;border-bottom:1px solid var(--line)}
.result-photo{width:230px;height:200px;flex:none;background:linear-gradient(180deg,#7fb3e0 0%,#b9d6ee 45%,#c7c9cc 46%,#8c8f94 100%)}
.result-body{flex:1;position:relative}
.result-body h3{font-size:14px;color:var(--ink);border-bottom:2px solid var(--ink);padding-bottom:6px}
.result-cols{display:flex;gap:24px;margin-top:12px}
.spec{border-collapse:collapse;width:290px;font-size:11.5px}
.spec th{width:70px;background:var(--grey);text-align:left;font-weight:500;padding:4px 8px;border-bottom:1px solid var(--white)}
.spec td{padding:4px 10px;border-bottom:1px solid var(--line)}
.result-text{flex:1;font-size:11.5px;line-height:1.8}
.btn-more{position:absolute;right:0;bottom:0;width:110px;height:30px;background:var(--yellow);border:2px solid var(--ink);font-family:"Montserrat",sans-serif;font-weight:700;font-size:12px;color:var(--ink);display:flex;align-items:center;justify-content:center}
.results-all{position:absolute;top:950px;left:470px;width:260px;height:50px}

/* cta */
.cta{top:3940px;height:180px;background:linear-gradient(90deg,#8f8a82 0%,#c9c4bb 50%,#a7a29a 100%)}
.cta-list{position:absolute;top:50px;left:170px;width:860px;display:flex;gap:60px}
.cta-btn{width:400px;height:80px;background:var(--white);border:2px solid var(--ink);display:flex;align-items:center}
.cta-btn .icon{width:78px;height:100%;background:var(--yellow);display:flex;align-items:center;justify-content:center;border-right:2px solid var(--ink)}
.cta-btn span{flex:1;text-align:center;font-size:18px;font-weight:700;color:var(--ink)}
.cta-btn .arrow{width:40px;display:flex;justify-content:center}

/* footer */
.site-footer{top:4120px;height:468px;background:var(--footer);color:#cfcfcf}
.footer-info{position:absolute;top:40px;left:40px;width:380px;font-size:11.5px;line-height:1.9}
.footer-info .brand{color:var(--white);font-size:30px;display:flex;align-items:center;gap:10px;margin-bottom:18px}
.footer-info .brand i{width:11px;height:11px;background:var(--yellow);display:block}
.footer-info .company{color:var(--white);font-weight:700;font-size:13px}
.footer-photo{position:absolute;top:40px;left:470px;width:240px;height:170px;background:linear-gradient(135deg,#5c5c5c 0%,#9a9a9a 55%,#6e6e6e 100%)}
.footer-nav{position:absolute;top:40px;left:870px;display:grid;grid-template-columns:140px 140px;gap:6px 0;font-size:12px}
.footer-nav a{color:#e6e6e6;text-decoration:none;padding-left:12px;position:relative}
.footer-nav a::before{content:"";position:absolute;left:0;top:8px;width:5px;height:5px;background:var(--yellow)}
.copyright{position:absolute;bottom:0;left:0;width:100%;height:40px;background:#1d1d1d;text-align:center;line-height:40px;font-size:10px;color:#999}
</style>
</head>
<body>

<header class="section site-header">
  <div class="brand"><i></i>タカミエ</div>
  <p class="tagline">7階以上の新築分譲<br>マンション買取専門</p>
  <nav class="global-nav">
    <a>タカミエとは</a>
    <a>実績について</a>
    <a>買取実績</a>
    <a>会社概要</a>
    <div class="btn-reserve">
      <svg width="18" height="18" viewBox="0 0 18 18"><rect x="2" y="4" width="14" height="12" fill="none" stroke="#222" stroke-width="2"/><line x1="2" y1="8" x2="16" y2="8" stroke="#222" stroke-width="2"/><line x1="6" y1="2" x2="6" y2="6" stroke="#222" stroke-width="2"/><line x1="12" y1="2" x2="12" y2="6" stroke="#222" stroke-width="2"/></svg>
      ご来店予約
    </div>
  </nav>
</header>

<section class="section hero" role="img" aria-label="明るい窓辺のマンションの一室で本を読んで過ごす女性の写真">
  <div class="hero-copy">
    <p>7階以上の新築、買い取ります。</p>
    <div class="brand"><i></i>タカミエ</div>
  </div>
</section>
<div class="section slider-dots"><span></span><span></span><span></span><span></span></div>

<section class="section intro">
  <p>「タカミエ」は、7階以上の新築分譲のマンション買取サービスです。<br>眺望のよい高層階のマンションは、そのエリアでも希少で人気の高い住まいです。<br>「タカミエ」は、その価値を正しく査定し、スピーディーに買い取らせていただきます。</p>
</section>

<section class="section points" role="img" aria-label="ソファのある明るいリビングルームの写真">
  <div class="point-list">
    <article class="point-card">
      <div class="point-head"><div class="point-tag"><small>POINT</small><b>01</b></div><h3>新築の金額をご提示します！</h3></div>
      <p>高層階マンションならではの価値をしっかり評価し、新築時の価格を基準にした金額をご提示いたします。</p>
    </article>
    <article class="point-card">
      <div class="point-head"><div class="point-tag"><small>POINT</small><b>02</b></div><h3>売買もスムーズ！<br>すぐに現金化できます</h3></div>
      <p>当社が直接買い取るため、買主を探す必要がありません。ご契約から最短でのお引き渡しが可能です。</p>
    </article>
    <article class="point-card">
      <div class="point-head"><div class="point-tag"><small>POINT</small><b>03</b></div><h3>査定は無料！<br>仲介手数料もかかりません</h3></div>
      <p>査定のご依頼は無料です。直接買取のため、仲介手数料などの余計な費用も一切かかりません。</p>
    </article>
  </div>
  <div class="about-box">
    <h2><span class="brand">タカミエ</span>について</h2>
    <div class="btn-yellow">詳しくはこちら
      <svg width="12" height="12" viewBox="0 0 12 12"><path d="M3 1l6 5-6 5" fill="none" stroke="#222" stroke-width="2"/></svg>
    </div>
  </div>
</section>

<section class="section compare">
  <h2 class="slant-heading">
    <svg width="40" height="40" viewBox="0 0 40 40"><line x1="6" y1="4" x2="34" y2="36" stroke="#222" stroke-width="2"/></svg>
    一括見積りサイトとの違い
    <svg width="40" height="40" viewBox="0 0 40 40"><line x1="34" y1="4" x2="6" y2="36" stroke="#222" stroke-width="2"/></svg>
  </h2>

  <div class="compare-col col-sites">
    <div class="col-title">一括見積りサイト</div>
    <svg class="diagram" width="360" height="220" viewBox="0 0 360 220">
      <rect x="110" y="4" width="140" height="30" fill="#fff" stroke="#222" stroke-width="2"/>
      <text x="180" y="24" text-anchor="middle" font-size="12" font-weight="700" fill="#222">一括査定サイト</text>
      <g stroke="#222" stroke-width="1.5" fill="none">
        <line x1="180" y1="34" x2="180" y2="60"/>
        <line x1="40" y1="60" x2="320" y2="60"/>
        <line x1="40" y1="60" x2="40" y2="80"/><line x1="110" y1="60" x2="110" y2="80"/><line x1="180" y1="60" x2="180" y2="80"/><line x1="250" y1="60" x2="250" y2="80"/><line x1="320" y1="60" x2="320" y2="80"/>
        <line x1="40" y1="130" x2="40" y2="160"/><line x1="110" y1="130" x2="110" y2="160"/><line x1="180" y1="130" x2="180" y2="160"/><line x1="250" y1="130" x2="250" y2="160"/><line x1="320" y1="130" x2="320" y2="160"/>
      </g>
      <g fill="#8cc63f">
        <circle cx="40" cy="105" r="24"/><circle cx="110" cy="105" r="24"/><circle cx="180" cy="105" r="24"/><circle cx="250" cy="105" r="24"/><circle cx="320" cy="105" r="24"/>
      </g>
      <g font-size="9" fill="#fff" text-anchor="middle" font-weight="700">
        <text x="40" y="108">不動産</text><text x="110" y="108">不動産</text><text x="180" y="108">不動産</text><text x="250" y="108">不動産</text><text x="320" y="108">不動産</text>
      </g>
      <rect x="10" y="160" width="340" height="34" fill="#5f9a1f"/>
      <text x="180" y="182" text-anchor="middle" font-size="13" font-weight="700" fill="#fff">お客様</text>
    </svg>
    <ul class="reasons">
      <li><b>1</b>複数の会社に個人情報が渡るため、たくさんの電話や営業の連絡がきてしまい対応に追われます。</li>
      <li><b>2</b>最終的な価格は会社ごとに異なり、実際の売却までに時間がかかることもあります。</li>
    </ul>
  </div>

  <div class="compare-col col-ours">
    <div class="col-title">タカミエ</div>
    <svg class="diagram" width="360" height="250" viewBox="0 0 360 250">
      <circle cx="180" cy="100" r="90" fill="#f5d800"/>
      <text x="180" y="110" text-anchor="middle" font-size="28" font-weight="900" fill="#222" letter-spacing="2">タカミエ</text>
      <line x1="180" y1="190" x2="180" y2="210" stroke="#222" stroke-width="1.5"/>
      <rect x="10" y="210" width="340" height="34" fill="#f5d800"/>
      <text x="180" y="232" text-anchor="middle" font-size="13" font-weight="700" fill="#222">お客様</text>
    </svg>
    <ul class="reasons">
      <li><b>1</b>当社が直接お客様とやり取りするため、余計な営業の連絡は一切ありません。安心してご相談いただけます。</li>
      <li><b>2</b>自社買取なので査定から売却までがスピーディー。仲介手数料も不要です。</li>
    </ul>
  </div>
</section>

<section class="section faq">
  <div class="en-heading"><h2>FAQ</h2><p>よくある質問</p></div>
  <div class="faq-list">
    <article class="faq-card"><div class="faq-q"><span class="mark">Q</span><p>査定を依頼したら必ず売却しなければいけませんか？</p></div><div class="faq-a"><span class="mark">A</span><p>いいえ、査定のみでも大丈夫です。金額にご納得いただいてから売却をご判断ください。</p></div></article>
    <article class="faq-card"><div class="faq-q"><span class="mark">Q</span><p>7階未満のマンションでも相談できますか？</p></div><div class="faq-a"><span class="mark">A</span><p>当サービスは7階以上が対象です。それ以外の物件もまずはお気軽にご相談ください。</p></div></article>
    <article class="faq-card"><div class="faq-q"><span class="mark">Q</span><p>査定にはどのくらいの時間がかかりますか？</p></div><div class="faq-a"><span class="mark">A</span><p>物件の情報をいただければ、最短で当日中に査定結果をご案内いたします。</p></div></article>
    <article class="faq-card"><div class="faq-q"><span class="mark">Q</span><p>住宅ローンが残っていても売却できますか？</p></div><div class="faq-a"><span class="mark">A</span><p>はい、可能です。売却代金でローンを完済する方法などをご提案いたします。</p></div></article>
    <article class="faq-card"><div class="faq-q"><span class="mark">Q</span><p>来店せずに査定を依頼することはできますか？</p></div><div class="faq-a"><span class="mark">A</span><p>はい、お電話やフォームからのご依頼も承っております。お気軽にどうぞ。</p></div></article>
    <article class="faq-card"><div class="faq-q"><span class="mark">Q</span><p>売却後の費用や手続きはどうなりますか？</p></div><div class="faq-a"><span class="mark">A</span><p>必要な手続きは当社がサポートいたします。仲介手数料はかかりません。</p></div></article>
  </div>
</section>

<section class="section results">
  <div class="en-heading"><h2>RESULTS</h2><p>買取実績</p></div>
  <div class="result-list">
    <article class="result-item">
      <div class="result-photo" role="img" aria-label="青空の下に建つ高層マンションの外観写真"></div>
      <div class="result-body">
        <h3>大阪市北区の高層マンション 12階 3LDKを買取しました</h3>
        <div class="result-cols">
          <table class="spec"><tr><th>所在地</th><td>大阪市北区</td></tr><tr><th>階数</th><td>12階</td></tr><tr><th>間取り</th><td>3LDK</td></tr><tr><th>築年数</th><td>新築</td></tr><tr><th>買取期間</th><td>約2週間</td></tr></table>
          <p class="result-text">眺望のよい角部屋で、新築時の価格を基準に査定させていただきました。ご相談から約2週間でのお引き渡しとなり、お客様にもご満足いただけました。</p>
        </div>
        <div class="btn-more">MORE</div>
      </div>
    </article>
    <article class="result-item">
      <div class="result-photo" role="img" aria-label="青空の下に建つ高層マンションの外観写真"></div>
      <div class="result-body">
        <h3>大阪市中央区の高層マンション 15階 2LDKを買取しました</h3>
        <div class="result-cols">
          <table class="spec"><tr><th>所在地</th><td>大阪市中央区</td></tr><tr><th>階数</th><td>15階</td></tr><tr><th>間取り</th><td>2LDK</td></tr><tr><th>築年数</th><td>新築</td></tr><tr><th>買取期間</th><td>約10日</td></tr></table>
          <p class="result-text">転勤のため急ぎの売却をご希望でした。当社の直接買取により、短い期間でスムーズに現金化することができました。</p>
        </div>
        <div class="btn-more">MORE</div>
      </div>
    </article>
    <article class="result-item">
      <div class="result-photo" role="img" aria-label="青空の下に建つ高層マンションの外観写真"></div>
      <div class="result-body">
        <h3>大阪市西区の高層マンション 20階 3LDKを買取しました</h3>
        <div class="result-cols">
          <table class="spec"><tr><th>所在地</th><td>大阪市西区</td></tr><tr><th>階数</th><td>20階</td></tr><tr><th>間取り</th><td>3LDK</td></tr><tr><th>築年数</th><td>新築</td></tr><tr><th>買取期間</th><td>約3週間</td></tr></table>
          <p class="result-text">高層階からの夜景が魅力の物件です。複数の会社に相談されていましたが、当社の査定金額にご納得いただきました。</p>
        </div>
        <div class="btn-more">MORE</div>
      </div>
    </article>
  </div>
  <div class="btn-yellow results-all">買取実績をもっと見る
    <svg width="12" height="12" viewBox="0 0 12 12"><path d="M3 1l6 5-6 5" fill="none" stroke="#222" stroke-width="2"/></svg>
  </div>
</section>

<section class="section cta" role="img" aria-label="マンション室内のダイニングの写真">
  <div class="cta-list">
    <div class="cta-btn">
      <div class="icon"><svg width="34" height="34" viewBox="0 0 34 34"><rect x="6" y="4" width="22" height="26" fill="none" stroke="#222" stroke-width="2.5"/><line x1="11" y1="12" x2="23" y2="12" stroke="#222" stroke-width="2"/><line x1="11" y1="18" x2="23" y2="18" stroke="#222" stroke-width="2"/><line x1="11" y1="24" x2="19" y2="24" stroke="#222" stroke-width="2"/></svg></div>
      <span>買取無料査定はこちら</span>
      <div class="arrow"><svg width="12" height="14" viewBox="0 0 12 14"><path d="M2 1l8 6-8 6" fill="none" stroke="#222" stroke-width="2"/></svg></div>
    </div>
    <div class="cta-btn">
      <div class="icon"><svg width="34" height="34" viewBox="0 0 34 34"><rect x="4" y="7" width="26" height="23" fill="none" stroke="#222" stroke-width="2.5"/><line x1="4" y1="14" x2="30" y2="14" stroke="#222" stroke-width="2"/><line x1="11" y1="3" x2="11" y2="10" stroke="#222" stroke-width="2.5"/><line x1="23" y1="3" x2="23" y2="10" stroke="#222" stroke-width="2.5"/></svg></div>
      <span>ご来店予約はこちら</span>
      <div class="arrow"><svg width="12" height="14" viewBox="0 0 12 14"><path d="M2 1l8 6-8 6" fill="none" stroke="#222" stroke-width="2"/></svg></div>
    </div>
  </div>
</section>

<footer class="section site-footer">
  <div class="footer-info">
    <div class="brand"><i></i>タカミエ</div>
    <p class="company">運営：株式会社ヨツバリンク</p>
    <p>〒530-0000<br>大阪府大阪市北区中之島9丁目1-1<br>ヨツバビル 5F<br>TEL：06-0000-1234</p>
  </div>
  <div class="footer-photo" role="img" aria-label="店舗の相談カウンターの写真"></div>
  <nav class="footer-nav">
    <a>HOME</a><a>買取実績</a>
    <a>タカミエとは</a><a>会社概要</a>
    <a>実績について</a><a>プライバシーポリシー</a>
    <a>買取無料査定</a><a>お問合せ</a>
    <a>ご来店予約</a>
  </nav>
  <p class="copyright">Copyright © Yotsuba Link Co.,Ltd. All Rights Reserved.</p>
</footer>

</body>
</html>
```